Simple elegant feminine design - Going out on my own as a Mortgage Broker.
My thoughts are the following details on the Front, middle of the card possibly? Phone and email smaller font than my name?
Marnie Veltrin
Finance Specialist
p: 0438 215 962
e: marnie@veltrinlending.com.au
Bottom of the card
residential / commercial / equipment
I would like the Font in Rose Gold maybe white or black background? or Possibly a stone grey - are you able to do a few options? I'd like them embossed
Then I had an idea as a simple logo as per the attached if you get the idea in my scribble, my initials, capital M attached to a small v that leads/follows into a circle? Thicker Font In Rose Gold, middle of the card at the back.
Very open to ideas though and what colour you think would look better with the Rose Gold.
Thanks so much for your help, I am not very creative and savvy with this stuff :-)
Industry/Entity Type
Finance
Contact Information for Business Card
Marnie Veltrin
p: 0438 215 962
Look and feel

```html
<!DOCTYPE html>
<html lang="en">
<head>
<meta charset="utf-8">
<title>Marnie's Business Cards</title>
<link href="https://fonts.googleapis.com/css2?family=Montserrat:wght@300;400&display=swap" rel="stylesheet">
<style>
  :root {
    --backdrop: #eeeeee;
    --card-dark: #222325;
    --card-light: #ffffff;
    --rose-deep: #b07377;
    --rose-mid: #c98f88;
    --rose-light: #ecc6b9;
    --rose-text: #d9a79d;
    --rose-gradient: linear-gradient(100deg, #a8686e 0%, #e7bdb1 45%, #b97c7c 70%, #e3b4a8 100%);
  }
  * { margin: 0; padding: 0; box-sizing: border-box; }
  html, body { width: 1000px; height: 1200px; overflow: hidden; }
  body {
    background: var(--backdrop);
    font-family: 'Montserrat', sans-serif;
    position: relative;
  }
  .card {
    position: absolute;
    left: 268px;
    width: 464px;
    height: 278px;
    background: var(--card-dark);
  }
  .card--front { top: 90px; }
  .card--back { top: 463px; }
  .card--light { top: 830px; background: var(--card-light); }

  .brand-mark {
    position: absolute;
    border: 2px solid var(--rose-mid);
    border-radius: 50%;
    display: flex;
    align-items: center;
    justify-content: center;
    text-align: center;
  }
  .brand-mark__name {
    font-family: 'Montserrat', sans-serif;
    font-weight: 400;
    color: var(--rose-mid);
    letter-spacing: 0.08em;
    text-transform: uppercase;
    line-height: 1.35;
  }
  .brand-mark--large { width: 106px; height: 106px; left: 179px; top: 67px; }
  .brand-mark--large .brand-mark__name { font-size: 10px; }
  .brand-mark--small { width: 88px; height: 88px; left: 45px; top: 100px; }
  .brand-mark--small .brand-mark__name { font-size: 8.5px; }

  .identity {
    position: absolute;
    text-align: center;
  }
  .identity--centred { left: 0; right: 0; top: 190px; }
  .identity__name {
    font-weight: 300;
    font-size: 24px;
    letter-spacing: 0.03em;
    text-transform: uppercase;
    background: var(--rose-gradient);
    -webkit-background-clip: text;
    background-clip: text;
    color: transparent;
    white-space: nowrap;
  }
  .identity__role {
    display: flex;
    align-items: center;
    justify-content: center;
    gap: 4px;
    margin-top: 6px;
    font-weight: 400;
    font-size: 11.5px;
    letter-spacing: 0.08em;
    text-transform: uppercase;
    color: var(--rose-text);
  }
  .identity__rule {
    width: 30px;
    height: 1px;
    background: var(--rose-mid);
  }
  .card--light .identity__role { color: var(--rose-deep); }

  .divider {
    position: absolute;
    left: 168px;
    top: 72px;
    width: 2px;
    height: 170px;
    background: linear-gradient(180deg, var(--rose-light), var(--rose-deep));
  }
  .identity--beside { left: 185px; top: 80px; text-align: left; }
  .identity--beside .identity__role { justify-content: flex-start; }

  .contact {
    position: absolute;
    left: 185px;
    top: 150px;
    font-size: 11.5px;
    font-weight: 400;
    color: var(--rose-text);
    list-style: none;
  }
  .contact__item {
    display: flex;
    align-items: center;
    gap: 8px;
    height: 29px;
  }
  .contact__icon { width: 15px; height: 13px; flex: none; }
  .services {
    position: absolute;
    left: 185px;
    top: 214px;
    font-size: 11.5px;
    color: var(--rose-text);
    letter-spacing: 0.02em;
  }
</style>
</head>
<body>

  <section class="card card--front" aria-label="Business card front, dark">
    <div class="brand-mark brand-mark--large"><span class="brand-mark__name">Veltrin<br>Lending</span></div>
    <div class="identity identity--centred">
      <h1 class="identity__name">Marnie Veltrin</h1>
      <p class="identity__role"><span class="identity__rule"></span>Finance Specialist<span class="identity__rule"></span></p>
    </div>
  </section>

  <section class="card card--back" aria-label="Business card back, dark">
    <div class="brand-mark brand-mark--small"><span class="brand-mark__name">Veltrin<br>Lending</span></div>
    <div class="divider"></div>
    <div class="identity identity--beside">
      <h2 class="identity__name">Marnie Veltrin</h2>
      <p class="identity__role"><span class="identity__rule"></span>Finance Specialist<span class="identity__rule"></span></p>
    </div>
    <ul class="contact">
      <li class="contact__item">
        <svg class="contact__icon" viewBox="0 0 24 24" aria-hidden="true"><path fill="#d9a79d" d="M6.6 10.8c1.4 2.8 3.8 5.1 6.6 6.6l2.2-2.2c.3-.3.7-.4 1-.2 1.1.4 2.3.6 3.6.6.6 0 1 .4 1 1V20c0 .6-.4 1-1 1C10.6 21 3 13.4 3 4c0-.6.4-1 1-1h3.5c.6 0 1 .4 1 1 0 1.3.2 2.5.6 3.6.1.3 0 .7-.2 1z"/></svg>
        <span>0438 215 962</span>
      </li>
      <li class="contact__item">
        <svg class="contact__icon" viewBox="0 0 24 18" aria-hidden="true"><rect x="1" y="1" width="22" height="16" fill="#d9a79d"/><path d="M1 1l11 9 11-9" fill="none" stroke="#222325" stroke-width="1.5"/></svg>
        <span>marnie@veltrinlending.com.au</span>
      </li>
    </ul>
    <p class="services">residential / commercial / equipment</p>
  </section>

  <section class="card card--light" aria-label="Business card front, white">
    <div class="brand-mark brand-mark--large"><span class="brand-mark__name">Veltrin<br>Lending</span></div>
    <div class="identity identity--centred">
      <h2 class="identity__name">Marnie Veltrin</h2>
      <p class="identity__role"><span class="identity__rule"></span>Finance Specialist<span class="identity__rule"></span></p>
    </div>
  </section>

</body>
</html>
```